Anesthesia Medical Practice Business Card

We need a business card to hand out to surgeons with my basic information. Something that stands out but is not over the top. The medical community is rather conservative. I'd like them to call me first when flipping through their rolodex of anesthesiologists. I'd like the card to communicate confidence, control, professionalism yet serenity. I don't want the card to be pricey to print.

he logo will be provided as a vector graphic in addition to a complete business card design including the logo

Rex Alba Tovell, M.D.
Board Certified Anesthesiologist

(555) 638-2175

rtovell@quillnet.example

Mailing Address:
48317 Pemberly Ave.
Suite 274-6583
Los Angeles, CA 90871

A logo that inegrates my initials perhaps
RT MD
My initials are RT and MD as in Medical Doctor

or
perhaps a physician in surgical mask and cap caring for a patient

Surgeons who need anesthesia services

Medical

• the logo will be provided as a vector graphic in addition to a complete business card design including the logo

Rex Alba Tovell, M.D.

(555) 638-2175

rtovell@quillnet.example

Mailing Address:
48317 Pemberly Ave.
Suite 274-6583
Los Angeles, CA 90871

• A logo that inegrates my initials perhaps
RT MD

or

```html
<!DOCTYPE html>
<html lang="en">
<head>
<meta charset="utf-8">
<title>Rex Alba Tovell, M.D. — Business Card</title>
<link rel="stylesheet" href="https://fonts.googleapis.com/css2?family=Open+Sans:wght@400;600;700&display=swap">
<style>
  :root {
    --backdrop: #d9dbdd;
    --card: #ffffff;
    --teal: #5bbfc7;
    --slate: #5c6865;
    --rule: #b9c0bf;
  }
  * { box-sizing: border-box; margin: 0; padding: 0; }
  html, body {
    width: 1200px; height: 900px; overflow: hidden;
    background: var(--backdrop);
    font-family: "Open Sans", Arial, sans-serif;
  }
  .stage {
    width: 1200px; height: 900px;
    display: flex; align-items: center; justify-content: center; gap: 40px;
  }
  .card {
    position: relative;
    width: 540px; height: 320px;
    background: var(--card);
    border-radius: 30px;
    box-shadow: 0 2px 6px rgba(0,0,0,0.12);
  }

  /* Front: name mark inside a plain ring */
  .card-front .brand {
    position: absolute; left: 150px; top: 40px;
    width: 240px; height: 240px;
    display: flex; align-items: center; justify-content: center;
    text-align: center;
  }
  .card-front .brand svg { position: absolute; inset: 0; }
  .card-front .brand-name {
    position: relative;
    font-size: 26px; font-weight: 700; color: var(--slate);
    line-height: 1.25;
  }

  /* Back */
  .card-back .badge {
    position: absolute; left: 40px; top: 95px;
    width: 130px; height: 130px;
    display: flex; align-items: center; justify-content: center;
    text-align: center;
  }
  .card-back .badge svg { position: absolute; inset: 0; }
  .card-back .badge-name {
    position: relative;
    font-size: 15px; font-weight: 700; color: var(--slate); line-height: 1.2;
  }
  .details {
    position: absolute; left: 232px; top: 58px;
    padding-left: 18px;
    border-left: 1px solid var(--rule);
    color: var(--slate);
    font-size: 14px; line-height: 1.3;
  }
  .details .name { color: var(--teal); font-size: 17px; }
  .details .title { margin-bottom: 18px; }
  .contact-row { display: flex; align-items: center; gap: 8px; }
  .contact-row svg { width: 12px; height: 12px; flex: none; }
  .mailing {
    margin-top: 12px; margin-left: 22px;
    padding-left: 12px;
    border-left: 1px solid var(--rule);
  }
  .mailing .label { color: var(--teal); }
</style>
</head>
<body>
<main class="stage">

  <section class="card card-front" aria-label="Card front">
    <div class="brand">
      <svg viewBox="0 0 240 240" aria-hidden="true">
        <circle cx="120" cy="120" r="116" fill="none" stroke="var(--teal)" stroke-width="4"/>
      </svg>
      <span class="brand-name">Rex Alba<br>Tovell, M.D.</span>
    </div>
  </section>

  <section class="card card-back" aria-label="Card back">
    <div class="badge">
      <svg viewBox="0 0 130 130" aria-hidden="true">
        <circle cx="65" cy="65" r="62" fill="none" stroke="var(--teal)" stroke-width="3"/>
      </svg>
      <span class="badge-name">Rex Alba<br>Tovell</span>
    </div>

    <div class="details">
      <p class="name">Rex Alba Tovell, M.D.</p>
      <p class="title">Board Certified Anesthesiologist</p>

      <p class="contact-row">
        <svg viewBox="0 0 12 12" aria-hidden="true">
          <rect width="12" height="12" rx="2" fill="var(--slate)"/>
          <path d="M3.2 2.6l1.4 0 .6 1.8-.9.7a5 5 0 0 0 2.6 2.6l.7-.9 1.8.6 0 1.4c-3.6.3-6.5-2.6-6.2-6.2z" fill="#fff"/>
        </svg>
        (555) 638-2175
      </p>
      <p class="contact-row">
        <svg viewBox="0 0 12 12" aria-hidden="true">
          <rect y="2" width="12" height="8" rx="1" fill="var(--slate)"/>
          <path d="M1 3l5 4 5-4" fill="none" stroke="#fff" stroke-width="1"/>
        </svg>
        rtovell@quillnet.example
      </p>

      <div class="mailing">
        <p class="label">Mailing Address:</p>
        <p>48317 Pemberly Ave.</p>
        <p>Suite 274-6583</p>
        <p>Los Angeles, CA 90871</p>
      </div>
    </div>
  </section>

</main>
</body>
</html>
```